Flash Banner TRV - Velvet Coin Rotor

Hello at all, i need a flash banner (animated) for my site [url removed, login to view]
I want that everyone will made 2 banners:

- one at your imagination, write all that you want also in english.

- one with write "Non perdere tempo... Il tempo è denaro... Il denaro lo trovi su Rotor." ("Don't loose time... Time is money...Money you find in Rotor.")
here you can use images of time, money, dollar....

Banner must be in Italian Language and size must be 1260 x 300

Of course, for both banners, there must be my logo (zip file) and my motto ("I tuoi investimenti... mai stati così sicuri.")

for winner there is a good award:

- 150$ for contest
- a bonus of 150$ to spent in my site. This 150$ will became 300$.

Then, in total 450$ for winner.

As always... open your imagination... :P

Good work at all

```html
<!DOCTYPE html>
<html lang="it">
<head>
<meta charset="utf-8">
<title>Velvet Coin Rotor</title>
<link href="https://fonts.googleapis.com/css2?family=Bebas+Neue&family=Arimo:ital,wght@0,400;1,700&family=Tinos:ital,wght@1,700&display=swap" rel="stylesheet">
<style>
  :root {
    --charcoal: #3a3b3d;
    --side-green: #2f9d3b;
    --deep-green: #0b4a22;
    --mid-green: #16702f;
    --logo-green: #3fae3a;
    --motto-red: #d8201f;
    --motto-green: #37a82f;
    --nav-top: #f6f6f6;
    --nav-bottom: #d9d9d9;
    --nav-text: #4a4a4a;
    --button-top: #4fd04a;
    --button-bottom: #1e9a1f;
    --white: #ffffff;
  }
  * { margin: 0; padding: 0; box-sizing: border-box; }
  html, body { width: 1200px; height: 776px; overflow: hidden; }
  body { position: relative; background: var(--charcoal); font-family: "Arimo", Arial, sans-serif; }

  .site-header { position: absolute; left: 0; top: 0; width: 1200px; height: 200px; }
  .brand {
    position: absolute; left: 0; width: 1200px; top: 58px;
    display: flex; justify-content: center; align-items: center; gap: 14px;
  }
  .brand-dot { width: 34px; height: 34px; border-radius: 50%; background: var(--logo-green); }
  .brand-name { font-family: "Bebas Neue", sans-serif; font-size: 58px; color: var(--logo-green); line-height: 1; }
  .motto {
    position: absolute; left: 0; width: 1200px; top: 166px; text-align: center;
    font-family: "Tinos", "Times New Roman", serif; font-style: italic; font-weight: 700; font-size: 20px;
    color: var(--motto-red);
  }
  .motto .accent { color: var(--motto-green); }

  .hero-band { position: absolute; left: 0; top: 200px; width: 1200px; height: 469px; background: var(--side-green); }
  .hero {
    position: absolute; left: 24px; top: 0; width: 1140px; height: 469px;
    background: radial-gradient(ellipse at 50% 40%, var(--mid-green) 0%, var(--deep-green) 75%);
  }
  .hero-logo {
    position: absolute; left: 0; width: 1140px; top: 160px;
    display: flex; justify-content: center; align-items: center; gap: 18px;
  }
  .hero-logo-dot { width: 56px; height: 56px; border-radius: 50%; background: var(--white); }
  .hero-logo-name { font-family: "Bebas Neue", sans-serif; font-size: 72px; color: var(--white); line-height: 1; }
  .headline {
    position: absolute; left: 0; width: 1140px; top: 330px; text-align: center;
    font-family: "Bebas Neue", sans-serif; font-size: 64px; color: var(--white); letter-spacing: 1px;
  }

  .main-nav {
    position: absolute; left: 24px; top: 669px; width: 1140px; height: 84px;
    background: linear-gradient(var(--nav-top), var(--nav-bottom));
  }
  .nav-item { position: absolute; top: 32px; font-size: 17px; color: var(--nav-text); }
  .nav-item.active {
    top: 23px; left: 33px; width: 80px; height: 36px; border-radius: 5px;
    background: linear-gradient(var(--button-top), var(--button-bottom));
    color: var(--white); text-align: center; line-height: 36px;
  }
  .content { position: absolute; left: 24px; top: 753px; width: 1140px; height: 23px; background: var(--white); }
  .last-paid { position: absolute; left: 676px; top: 4px; font-size: 15px; font-style: italic; font-weight: 700; color: #333; }
</style>
</head>
<body>
  <header class="site-header">
    <div class="brand">
      <span class="brand-dot"></span>
      <span class="brand-name">Velvet Coin</span>
    </div>
    <p class="motto">I tuoi <span class="accent">investimenti...</span> mai stati <span class="accent">così</span> sicuri.</p>
  </header>

  <section class="hero-band">
    <div class="hero" role="img" aria-label="Deep green banner background with faint dollar sign pattern">
      <div class="hero-logo">
        <span class="hero-logo-dot"></span>
        <span class="hero-logo-name">Velvet Coin Rotor</span>
      </div>
      <h1 class="headline">IL DENARO LO TROVI SU ROTOR</h1>
    </div>
  </section>

  <nav class="main-nav">
    <span class="nav-item active">Home</span>
    <span class="nav-item" style="left:151px">Signup</span>
    <span class="nav-item" style="left:259px">Login</span>
    <span class="nav-item" style="left:356px">Prossimi al pagamento</span>
    <span class="nav-item" style="left:580px">Membri Pagati</span>
    <span class="nav-item" style="left:743px">Notizie</span>
    <span class="nav-item" style="left:848px">FAQ</span>
    <span class="nav-item" style="left:937px">Contattaci</span>
  </nav>

  <main class="content">
    <p class="last-paid">Last Paid Members :</p>
  </main>
</body>
</html>
```